Real estate investor, needing a business card that communicates warmth, integrity, empathy.

I have a logo that can be manipulated to align with the message - "Serving your home selling needs." Want it to stand out from typical real estate investor cards, and make distressed home sellers feel a connection with me. Should communicate warmth, integrity, empathy, and trustworthiness.

Target Market(s)

Distressed home owners who need to sell their homes, not using realtors.

Contact Information for Business Card

Glossy front and matte back, with a small box that is labelled "notes." I like darker blues and blacks together, but doesn't have to be, as long as it communicates trustworthiness, and a strong call to action.

Other font styles liked:
• see "must haves" above, but willing to review whatever comes my way.

Requirements
Must have
• The fonts on my logo are Aviano, Lusitana, and Marcellus. We don't have to use those, but I favor them.

```html
<!DOCTYPE html>
<html lang="en">
<head>
<meta charset="utf-8">
<title>Ridgeline Home Buyers — Business Card</title>
<link rel="stylesheet" href="https://fonts.googleapis.com/css2?family=Lusitana:wght@400;700&display=swap">
<style>
  :root {
    --page-bg: #efefef;
    --card-bg: #0e0e10;
    --ink: #ffffff;
    --bronze: #a67c52;
    --serif: "Lusitana", Georgia, serif;
  }
  * { margin: 0; padding: 0; box-sizing: border-box; }
  html, body {
    width: 761px; height: 1200px; overflow: hidden;
    background: var(--page-bg);
    font-family: var(--serif);
  }
  .canvas { position: relative; width: 761px; height: 1200px; }

  .card {
    position: absolute; left: 60px; width: 640px; height: 365px;
    background: var(--card-bg);
    box-shadow: 0 2px 6px rgba(0,0,0,.25);
    overflow: hidden; color: var(--ink);
  }
  .card--front { top: 200px; }
  .card--back  { top: 636px; }

  .brand-name {
    position: absolute; text-align: center;
    font-family: var(--serif); font-weight: 700; color: var(--ink);
    letter-spacing: .06em; line-height: 1.15;
  }
  .card--front .brand-name { left: 0; right: 0; top: 110px; font-size: 34px; }
  .card--back .brand-name { left: 40px; width: 262px; top: 150px; font-size: 27px; }
  .brand-name small { display: block; font-size: .62em; letter-spacing: .08em; }

  .tagline {
    position: absolute; left: 0; right: 0; top: 272px;
    text-align: center; font-size: 20px; letter-spacing: .01em;
  }
  .band-wide {
    position: absolute; left: 0; right: 0; top: 328px; height: 13px;
    background: var(--bronze);
  }
  .band-thin {
    position: absolute; left: 0; right: 0; bottom: 0; height: 7px;
    background: var(--bronze);
  }

  .divider {
    position: absolute; left: 331px; top: 86px; width: 1px; height: 193px;
    background: var(--ink);
  }
  .person-name {
    position: absolute; left: 374px; top: 92px;
    font-size: 35px; font-weight: 400; letter-spacing: .01em;
  }
  .person-role {
    position: absolute; left: 375px; top: 137px;
    font-size: 21px; color: var(--bronze);
  }
  .contact-list { position: absolute; left: 376px; top: 188px; list-style: none; }
  .contact-item {
    display: flex; align-items: center; height: 33px;
    font-size: 13px;
  }
  .contact-item--phone { font-size: 18px; }
  .contact-icon { width: 21px; height: 21px; margin-right: 14px; flex: none; }
</style>
</head>
<body>
<main class="canvas">

  <section class="card card--front" aria-label="Card front">
    <div class="brand-name">RIDGELINE<small>Home Buyers</small></div>
    <p class="tagline">SERVING YOUR HOME SELLING NEEDS</p>
    <div class="band-wide"></div>
  </section>

  <section class="card card--back" aria-label="Card back">
    <div class="brand-name">RIDGELINE<small>Home Buyers</small></div>
    <div class="divider"></div>
    <h1 class="person-name">Lorem ipsum</h1>
    <p class="person-role">Director</p>
    <ul class="contact-list">
      <li class="contact-item contact-item--phone">
        <svg class="contact-icon" viewBox="0 0 22 22" aria-hidden="true">
          <circle cx="11" cy="11" r="10" fill="none" stroke="#a67c52" stroke-width="1.2"/>
          <path d="M7.5 6.5c.6-.6 1.2-.5 1.6.1l.8 1.3c.3.5.2 1-.2 1.3l-.5.4c.5 1.2 1.5 2.2 2.7 2.7l.4-.5c.3-.4.8-.5 1.3-.2l1.3.8c.6.4.7 1 .1 1.6-.8.9-1.9 1-3 .5-2-.9-3.6-2.5-4.5-4.5-.5-1.1-.4-2.2.5-3z" fill="#ffffff"/>
        </svg>123-456-7890</li>
      <li class="contact-item">
        <svg class="contact-icon" viewBox="0 0 22 22" aria-hidden="true">
          <circle cx="11" cy="11" r="10" fill="none" stroke="#a67c52" stroke-width="1.2"/>
          <rect x="6" y="7.5" width="10" height="7" rx="1" fill="#ffffff"/>
          <path d="M6.3 8l4.7 3.6L15.7 8" fill="none" stroke="#0e0e10" stroke-width="1"/>
        </svg>info@ridgelinehomebuyers.com</li>
      <li class="contact-item">
        <svg class="contact-icon" viewBox="0 0 22 22" aria-hidden="true">
          <circle cx="11" cy="11" r="10" fill="none" stroke="#a67c52" stroke-width="1.2"/>
          <g fill="none" stroke="#ffffff" stroke-width=".9">
            <circle cx="11" cy="11" r="5"/>
            <ellipse cx="11" cy="11" rx="2.2" ry="5"/>
            <path d="M6 11h10M7 8.5h8M7 13.5h8"/>
          </g>
        </svg>www.ridgelinehomebuyers.com</li>
    </ul>
    <div class="band-thin"></div>
  </section>

</main>
</body>
</html>
```